Political sign design, fonts colors and layout

I am running for Town Council.

My message is done, and *a draft is attached* with the text we wish to use. It says "Elect Dana Velmont" etc. In Maroon and White. I am not a designer, but this is somewhat close to what we are looking for.

I need help with colors and fonts, layout, spacing, and general cleanup.

I'm attaching the town high school logo:

- "H" for Brookfield: with black and white outlines on the fonts
- we want to incorporate the black and white on the fonts
- for the entire text, parts of the text, or best would be a mix

This is for signs printed and placed all over my town.

We need two versions

1. square, 4' by 4' version
2. 36" by 24" version

The smaller version will drop the three bullet pointed text, but otherwise can be identical.

The sign can only use 3 printed colors (due to printing costs.)

1. maroon,
2. white,
3. black.

The maroon should match the maroon from the high school logo attached, which I believe I did in the draft.

We also like the white border around the outside, like in the "scoreboard" design attached.

Thanks for your attention, wish me luck.

Dana

Target Market(s)

SIgns, Political market

Industry/Entity Type

Political

Font styles to use
Sans Serif
Other font styles liked:
• Arial Black, Sans Serif Bold

Requirements
Must have
• maroon background, white font.
• - black borders around fonts where appropriate
• - great spacing
• - great typeface usage
• - clean and crisp political sign, visible while driving.
• - my name "Dana Velmont" much larger like the draft, or the appropriate additional size
• - two versions, one square, and one 36" / 24"
Nice to have
• - nice borders
• - dress it up a bit, using italics and bold fonts, without making it flashy or busy.
Should not have
• Must be easily readable from a car, except for "Paid for by Friends of Dana Velmont" which can be tiny.
• Colors are noted in the description, the "Brookfield Maroon" as the background, white font, and some use of black.

```html
<!DOCTYPE html>
<html lang="en">
<head>
<meta charset="utf-8">
<title>Elect Dana Velmont – Brookfield Council Sign</title>
<link rel="stylesheet" href="https://fonts.googleapis.com/css2?family=Graduate&family=Bowlby+One&family=Kaushan+Script&family=Yellowtail&family=Archivo+Black&family=Montserrat:wght@600;800&display=swap">
<style>
  :root {
    --brookfield-maroon: #72102f;
    --sign-white: #ffffff;
    --sign-black: #1b1b1b;
    --backdrop: #d9d9d9;
  }
  html, body {
    margin: 0;
    width: 1200px;
    height: 1200px;
    overflow: hidden;
    background: var(--backdrop);
  }
  .sign { display: block; width: 1200px; height: 1200px; }
  .sign__border { fill: var(--sign-white); }
  .sign__field { fill: var(--brookfield-maroon); }
  .headline {
    font-family: "Bowlby One", "Archivo Black", sans-serif;
    fill: var(--sign-white);
  }
  .script {
    font-family: "Kaushan Script", "Yellowtail", cursive;
    font-style: italic;
    fill: var(--sign-black);
    stroke: var(--sign-white);
    paint-order: stroke fill;
    stroke-linejoin: round;
  }
  .swoosh { fill: var(--sign-black); stroke: var(--sign-white); stroke-width: 4; stroke-linejoin: round; }
  .candidate-name { font-family: "Graduate", "Archivo Black", sans-serif; }
  .candidate-name--outer { fill: var(--sign-black); stroke: var(--sign-black); stroke-width: 22; stroke-linejoin: round; }
  .candidate-name--inner { fill: var(--brookfield-maroon); stroke: var(--sign-white); stroke-width: 10; paint-order: stroke fill; stroke-linejoin: round; }
  .office-band { fill: var(--sign-black); }
  .office-band__text {
    font-family: "Archivo Black", sans-serif;
    font-size: 21px;
    letter-spacing: 5px;
    fill: var(--sign-white);
  }
  .rule { fill: var(--sign-white); }
  .website {
    font-family: "Archivo Black", sans-serif;
    font-size: 30px;
    letter-spacing: 9px;
    fill: var(--sign-white);
  }
  .platform {
    font-family: "Montserrat", sans-serif;
    font-weight: 600;
    font-size: 23px;
    letter-spacing: 3.5px;
    fill: var(--sign-white);
  }
  .disclaimer {
    font-family: "Montserrat", sans-serif;
    font-weight: 600;
    font-size: 12px;
    letter-spacing: 1.5px;
    fill: var(--sign-white);
  }
</style>
</head>
<body>
<svg class="sign" viewBox="0 0 1200 1200" xmlns="http://www.w3.org/2000/svg" role="img" aria-label="Elect Dana Velmont for Brookfield Councilman / Trustee campaign sign">
  <rect class="sign__border" x="0" y="200" width="1200" height="800"/>
  <rect class="sign__field" x="16" y="216" width="1168" height="768"/>

  <!-- Slogan -->
  <text class="headline" x="77" y="334" font-size="58" textLength="820" lengthAdjust="spacingAndGlyphs">Take Back Our Town!</text>

  <!-- Elect -->
  <path class="swoosh" d="M906 344 C 990 336, 1060 322, 1106 296 C 1104 318, 1050 338, 966 362 Z"/>
  <text class="script" x="938" y="318" font-size="70" stroke-width="9" textLength="164" lengthAdjust="spacingAndGlyphs">Elect</text>

  <!-- Candidate name -->
  <text class="candidate-name candidate-name--outer" x="74" y="466" font-size="150" textLength="1040" lengthAdjust="spacingAndGlyphs">DANA VELMONT</text>
  <text class="candidate-name candidate-name--inner" x="74" y="466" font-size="150" textLength="1040" lengthAdjust="spacingAndGlyphs">DANA VELMONT</text>

  <!-- Office band -->
  <rect class="office-band" x="74" y="490" width="1048" height="48"/>
  <text class="office-band__text" x="598" y="522" text-anchor="middle">★ ★ ★  FOR BROOKFIELD COUNCILMAN / TRUSTEE  ★ ★ ★</text>

  <!-- Website -->
  <rect class="rule" x="70" y="571" width="268" height="22"/>
  <rect class="rule" x="848" y="571" width="274" height="22"/>
  <text class="website" x="594" y="593" text-anchor="middle">WWW.VELMONT.COM</text>

  <!-- Platform -->
  <text class="platform" x="598" y="650" text-anchor="middle">STOP HIGH TAXES • CLEAN UP OUR GOVERNMENT</text>
  <text class="platform" x="598" y="677" text-anchor="middle">PRESERVE OUR NEIGHBORHOODS</text>

  <!-- Fighting for Brookfield -->
  <path class="swoosh" d="M592 836 C 700 824, 860 814, 960 812 L 958 824 C 850 826, 700 832, 596 846 Z"/>
  <text class="script" x="164" y="800" font-size="96" stroke-width="10" textLength="820" lengthAdjust="spacingAndGlyphs">Fighting for Brookfield</text>

  <!-- Vote -->
  <text class="headline" x="176" y="932" font-size="60" textLength="848" lengthAdjust="spacingAndGlyphs">VOTE NOV. 8TH "ROW A"</text>

  <!-- Disclaimer -->
  <text class="disclaimer" x="600" y="970" text-anchor="middle">PAID FOR BY FRIENDS OF DANA</text>
</svg>
</body>
</html>
```